Need a new office flyer

I would like an 8.5 x 11" flyer made that can be emailed or printed out and handed to potential customers.  The flyer should include our existing logo and continuity of branding.   I am a commercial real estate broker and market myself to business with 5-50 employee's that are looking to buy or lease space to run their business from.  I focus my efforts on office & warehouse space. The flyer should have a banner "need a new location "
"VLD commercial real estate specializes in helping business and professionals buy/sell or lease  the best spaces for their business.  Take the stress & time out of finding the best location for your business and negotiating a great deal  VLD will do it for you and the best part our service is free to you. Working with VLD is easy as 1, 2, 3
1. Call, Text, Email us today and let us know what your looking to do.
2. VLD  will prepare a list of all the best available spaces that meet your specifications and set up tours of your favorites.
3. We will negotiate the best terms for your space. and help you with all the  details of getting your new space ready for you.
Don't forget the that our services are free to Buyers and Tenants so don't waste your companies time searching for locations, we already know where they are!
Contact us today!
Dale Norcutt
DRE 07354128
VLD Commercial Real Estate
555-317-4829
d.norcutt@vldprop-example.com

```html
<!DOCTYPE html>
<html lang="en">
<head>
<meta charset="utf-8">
<title>VLD Commercial Real Estate – We Are Moving</title>
<link rel="stylesheet" href="https://fonts.googleapis.com/css2?family=Montserrat:wght@400;500;600;700&family=Oswald:wght@700&display=swap">
<style>
  :root {
    --brand-blue: #2f6dab;
    --brand-blue-light: #dce8f4;
    --slate: #4b515c;
    --ink: #2b2b2b;
    --muted-grey: #8d8f93;
    --row-grey: #eeeeef;
    --footer-dark: #333333;
    --white: #ffffff;
    --page-bg: #ffffff;
  }
  * { box-sizing: border-box; margin: 0; padding: 0; }
  html, body { width: 800px; height: 1200px; overflow: hidden; background: var(--page-bg); }
  body { font-family: "Montserrat", Arial, sans-serif; color: var(--ink); }

  .flyer { position: relative; width: 800px; height: 1200px; overflow: hidden; background: var(--white); }

  /* Hero */
  .hero { position: absolute; inset: 0 0 auto 0; height: 500px; }
  .hero-art { position: absolute; inset: 0; }
  .brand { position: absolute; left: 42px; top: 44px; display: flex; align-items: center; gap: 12px; }
  .brand-dot { width: 58px; height: 58px; border-radius: 50%; background: var(--brand-blue); }
  .brand-name { font-weight: 700; font-size: 54px; color: var(--brand-blue); letter-spacing: 1px; line-height: 1; }
  .headline-kicker { position: absolute; left: 42px; top: 132px; font-weight: 600; font-size: 36px; color: var(--muted-grey); letter-spacing: 1px; }
  .headline { position: absolute; left: 38px; top: 160px; font-family: "Oswald", "Arial Narrow", sans-serif; font-weight: 700; font-size: 136px; line-height: 1.05; color: var(--brand-blue); letter-spacing: -1px; }
  .intro { position: absolute; left: 42px; top: 318px; width: 305px; font-size: 12.6px; line-height: 1.32; color: var(--ink); }

  /* Steps */
  .steps { position: absolute; left: 42px; top: 545px; width: 716px; list-style: none; display: flex; flex-direction: column; gap: 12px; }
  .step { display: flex; height: 88px; }
  .step-icon { width: 106px; background: var(--brand-blue); display: flex; align-items: center; justify-content: center; }
  .step--slate .step-icon, .step--slate .step-accent { background: var(--slate); }
  .step-body { flex: 1; display: flex; align-items: center; background: var(--row-grey); margin-left: 4px; box-shadow: 0 3px 4px rgba(0,0,0,0.12); }
  .step-num { width: 78px; text-align: center; font-size: 34px; font-weight: 500; color: var(--brand-blue); }
  .step--slate .step-num { color: var(--slate); }
  .step-divider { width: 1px; height: 56px; background: #c9c9cc; margin-right: 22px; }
  .step-text { font-size: 17px; line-height: 1.32; font-weight: 500; padding-right: 20px; }
  .step-accent { width: 20px; background: var(--brand-blue); }

  /* Banner */
  .note { position: absolute; left: 42px; top: 880px; width: 716px; height: 56px; border-radius: 8px; background: var(--brand-blue); color: var(--white); font-size: 14.4px; line-height: 1.3; text-align: center; display: flex; align-items: center; justify-content: center; padding: 0 20px; }

  /* Footer */
  .contact { position: absolute; left: 0; bottom: 0; width: 800px; height: 158px; background: var(--footer-dark); }
  .contact-tab { position: absolute; left: 236px; top: -18px; width: 326px; height: 40px; background: var(--brand-blue); border-radius: 0 0 6px 6px; color: var(--white); font-weight: 600; font-size: 25px; display: flex; align-items: center; justify-content: center; box-shadow: 0 3px 5px rgba(0,0,0,0.3); }
  .agent-photo { position: absolute; left: 42px; top: -16px; width: 122px; height: 142px; border: 4px solid var(--white); background: linear-gradient(160deg, #c9d8e6 0%, #7b93ad 55%, #253a60 100%); }
  .agent { position: absolute; left: 182px; top: 44px; list-style: none; color: var(--white); font-weight: 600; font-size: 17.5px; line-height: 28px; }
  .channels { position: absolute; left: 460px; top: 44px; list-style: none; color: var(--white); font-weight: 600; font-size: 17px; line-height: 28px; }
  .channels li { display: flex; align-items: center; gap: 10px; }
  .channels svg { flex: none; }
</style>
</head>
<body>
<main class="flyer">

  <section class="hero">
    <svg class="hero-art" width="800" height="500" viewBox="0 0 800 500" aria-hidden="true">
      <defs>
        <linearGradient id="sky" x1="0" y1="0" x2="1" y2="1">
          <stop offset="0" stop-color="#ffffff"/>
          <stop offset="0.6" stop-color="#eef3f9"/>
          <stop offset="1" stop-color="#d5e3f1"/>
        </linearGradient>
        <linearGradient id="tower" x1="0" y1="0" x2="0" y2="1">
          <stop offset="0" stop-color="#8fb0d2"/>
          <stop offset="0.5" stop-color="#3f6c99"/>
          <stop offset="1" stop-color="#1f3b5e"/>
        </linearGradient>
      </defs>
      <rect width="800" height="500" fill="url(#sky)"/>
      <polygon points="620,0 800,0 800,432 430,432" fill="url(#tower)" role="img" aria-label="Photo of glass office towers against a blue sky"/>
      <polygon points="330,432 620,0 620,432" fill="var(--brand-blue)" opacity="0.85"/>
      <rect x="0" y="432" width="800" height="68" fill="var(--white)"/>
    </svg>

    <div class="brand">
      <span class="brand-dot"></span>
      <span class="brand-name">VLD</span>
    </div>
    <p class="headline-kicker">WE ARE</p>
    <h1 class="headline">MOVING</h1>
    <p class="intro">VLD commercial real estate specializes in helping business and professionals buy/sell or lease the best spaces for their business. Take the stress &amp; time out of finding the best location for your business and negotiating a great deal VLD will do it for you and the best part our service is free to you.</p>
  </section>

  <ol class="steps">
    <li class="step">
      <div class="step-icon">
        <svg width="58" height="52" viewBox="0 0 58 52" fill="none" stroke="#fff" stroke-width="2.6" stroke-linecap="round" stroke-linejoin="round" aria-hidden="true">
          <path d="M6 14c-2 4 2 14 10 22s18 12 22 10l4-5-8-6-4 4c-4-1-11-8-12-12l4-4-6-8z"/>
          <path d="M26 4h22a6 6 0 0 1 6 6v10a6 6 0 0 1-6 6h-8l-6 6v-6h-8a6 6 0 0 1-6-6V10a6 6 0 0 1 6-6z"/>
        </svg>
      </div>
      <div class="step-body">
        <span class="step-num">01</span><span class="step-divider"></span>
        <p class="step-text">Call, Text, Email us today and let us know what your looking to do.</p>
      </div>
      <div class="step-accent"></div>
    </li>
    <li class="step step--slate">
      <div class="step-icon">
        <svg width="56" height="56" viewBox="0 0 56 56" fill="none" stroke="#fff" stroke-width="2.4" stroke-linejoin="round" stroke-linecap="round" aria-hidden="true">
          <path d="M6 26 28 14l22 12"/>
          <path d="M10 24v28h36V24"/>
          <rect x="16" y="36" width="10" height="16"/>
          <rect x="30" y="36" width="10" height="8"/>
          <circle cx="36" cy="28" r="3"/>
          <path d="M18 10V2M14 6l4-4 4 4M28 8V0M24 4l4-4 4 4M38 10V2M34 6l4-4 4 4"/>
        </svg>
      </div>
      <div class="step-body">
        <span class="step-num">02</span><span class="step-divider"></span>
        <p class="step-text">VLD will prepare a list of all the best available spaces that meet your specifications and set up tours of your favorites.</p>
      </div>
      <div class="step-accent"></div>
    </li>
    <li class="step">
      <div class="step-icon">
        <svg width="58" height="54" viewBox="0 0 58 54" fill="none" stroke="#fff" stroke-width="2.6" stroke-linecap="round" stroke-linejoin="round" aria-hidden="true">
          <path d="M20 4a16 16 0 1 0 8 30l8 4-3-9A16 16 0 0 0 20 4z"/>
          <path d="M15 16a5 5 0 1 1 7 5c-2 1-2 2-2 4"/>
          <circle cx="20" cy="30" r="0.8" fill="#fff"/>
          <path d="M38 20a14 14 0 0 1 8 26l3 7-8-4a14 14 0 0 1-12-4"/>
        </svg>
      </div>
      <div class="step-body">
        <span class="step-num">03</span><span class="step-divider"></span>
        <p class="step-text">We will negotiate the best terms for your space. and help you with all the details of getting your new space ready for you.</p>
      </div>
      <div class="step-accent"></div>
    </li>
  </ol>

  <p class="note">Don't forget the that our services are free to Buyers and Tenants so don't waste your companies time searching for locations, we already know where they are!</p>

  <footer class="contact">
    <div class="agent-photo" role="img" aria-label="Portrait photo of the agent in a navy suit"></div>
    <div class="contact-tab">Contact us today!</div>
    <ul class="agent">
      <li>Dale Norcutt</li>
      <li>DRE 07354128</li>
      <li>VLD Commercial Real Estate</li>
    </ul>
    <ul class="channels">
      <li>
        <svg width="14" height="14" viewBox="0 0 24 24" aria-hidden="true"><path fill="var(--brand-blue)" d="M6.6 10.8a15 15 0 0 0 6.6 6.6l2.2-2.2c.3-.3.7-.4 1-.2 1.1.4 2.3.6 3.6.6.6 0 1 .4 1 1V20c0 .6-.4 1-1 1A17 17 0 0 1 3 4c0-.6.4-1 1-1h3.5c.6 0 1 .4 1 1 0 1.3.2 2.5.6 3.6.1.3 0 .7-.2 1z"/></svg>
        555-317-4829
      </li>
      <li>
        <svg width="14" height="14" viewBox="0 0 24 24" aria-hidden="true"><rect x="2" y="5" width="20" height="14" rx="2" fill="var(--brand-blue)"/><path d="M3 6l9 7 9-7" fill="none" stroke="#333" stroke-width="1.6"/></svg>
        d.norcutt@vldprop-example.com
      </li>
      <li>
        <svg width="14" height="14" viewBox="0 0 24 24" fill="none" stroke="var(--brand-blue)" stroke-width="2" aria-hidden="true"><circle cx="12" cy="12" r="10"/><path d="M2 12h20M12 2c3 3 4 6.5 4 10s-1 7-4 10c-3-3-4-6.5-4-10s1-7 4-10z"/></svg>
        www.vldprop-example.com
      </li>
    </ul>
  </footer>

</main>
</body>
</html>
```